Landing page for Varkeno Computer Support

We need a high converting landing page for PPC campaign for Varkeno Computer Support. We are looking for a responsive page which works for PC, MACREL and Mobile devices. Main purpose of page will be to generate calls to our Toll free number. Users can also opt for chat with technician to resolve their issues but only CTA of page should be to generate call to our toll free number.
Current landing page we use is- https://brivolhelpdesk.example/varkeno-computer-support.html (called Link1 in text below)
We will need following in new landing page:
1. Disclaimer - This is legally mandatory near CTA
GadgetMender is an independent provider of technical support services for several third party brands. If your product is under warranty or not repair service maybe available at brand owner or official website. Use of names, trademarks is for reference only. We disclaim any ownership, right, affiliation or endorsement of or by any such third party products or brands.
2. New Image of Customer Service Rep. See Link1
3. Description/details of what support for Varkeno we provide. See Link1. You can take some or all content from link1
4. Testimonials
5. Chat option
6. Footer with following- Contact Info and copyright statement. See Link1
7. You can place trust building logo like Quorbel Shield and Safenook to your choice to increase effectiveness of landing page
Take ideas from http://pagezeal.example/landing-page-articles/the-anatomy-of-a-landing-page/. We can put whatever is necessary on new landing page to reach goal of high conversions.
Landing pages designs we like:
http://www.setup-shieldware.example/5829174/quorbel/quorbel-support.html
http://www.mentorfix.example/varkeno/varkeno_support/varkeno_help_support.php
http://simplegizmo.example/fix-computer/
New Details:
-----------------
I generally prefer white background for landing pages. You can also use grey and any other color which goes with it. In the end, goal is high conversion rate.
Updates
Since some of the designs posted have ability to collect email address, I would like to clarify that Only CTA is to call toll free number. We don't need to collect email addresses. Reason is 99.9% of customers will only reach out to us if they have an urgent and immediate problem to resolve. They will call toll free and get support via remote connection but won't send email. Very few will opt to chat with technician. Even if they send email, they will never buy our services because they would have contacted somebody else to solve their immediate problem via remote connection.
Thanks
Target Market(s)
Home users and small business
Industry/Entity Type
Building
Coding
Coded - Design and coding required
Look and feel

```html
<!DOCTYPE html>
<html lang="en">
<head>
<meta charset="utf-8">
<title>Varkeno Computer Support – eFixHaven</title>
<link rel="stylesheet" href="https://fonts.googleapis.com/css2?family=Lato:wght@300;400;700;900&family=Roboto:wght@400;500;700&display=swap">
<style>
:root{
  --blue:#2a86c4;
  --blue-dark:#1f6fa6;
  --ink:#222;
  --text:#444;
  --muted:#888;
  --line:#dcdcdc;
  --gold:#f5c21b;
  --plan-grey:#a3a3a3;
  --green:#34c24f;
  --footer-dark:#333;
  --footer-blue:#2a87c0;
  --footer-base:#222;
  --white:#fff;
}
*{margin:0;padding:0;box-sizing:border-box}
html,body{width:1200px;height:2428px;overflow:hidden}
body{position:relative;background:var(--white);font-family:"Lato",Arial,sans-serif;color:var(--text)}
.abs{position:absolute}
ul{list-style:none}

/* header */
.site-header{top:0;left:0;width:1200px;height:100px;border-bottom:3px solid var(--blue)}
.brand{left:138px;top:24px;display:flex;align-items:center;gap:10px}
.brand-mark{width:30px;height:30px;border-radius:50%;background:#6b6b6b}
.brand-name{font-size:32px;font-weight:700;color:var(--ink);letter-spacing:-.5px}
.tollfree{left:769px;top:22px;display:flex;gap:16px;align-items:center}
.tollfree-icon{width:48px;height:50px;background:var(--blue);display:flex;align-items:center;justify-content:center}
.tollfree-label{font-size:23px;font-weight:900;color:var(--ink);line-height:1;letter-spacing:.5px}
.tollfree-number{font-size:31px;font-weight:700;color:var(--blue);line-height:1.2}

/* hero */
.hero{top:103px;left:0;width:1200px;height:393px;border-bottom:4px solid var(--blue);
  background:linear-gradient(90deg,#f1f1f3 0%,#e4dcd6 25%,#d9c7b8 45%,#ece8e4 60%,#e9d2be 78%,#f4f4f5 100%)}
.hero-caption{left:212px;top:313px;font-size:26px;font-weight:700;color:var(--white);text-shadow:0 1px 3px rgba(0,0,0,.35)}
.hero-dots{left:577px;top:374px;display:flex;gap:6px}
.hero-dots span{width:9px;height:9px;background:var(--white);opacity:.8}
.hero-dots span.on{background:var(--blue);opacity:1}

/* offer */
.section-title{top:526px;left:138px;width:924px;display:flex;align-items:center;gap:18px;font-size:29px;font-weight:400;color:#666;letter-spacing:1px}
.section-title::before,.section-title::after{content:"";flex:1;border-top:2px dotted #ccc}
.section-title em{font-style:normal;color:var(--blue)}
.plans{top:599px;left:138px;width:924px;display:flex;justify-content:space-between}
.plan{width:296px}
.plan-tab{height:42px;background:linear-gradient(#eee,#c3c3c3);text-align:center;font-size:21px;line-height:42px;color:#555;text-transform:uppercase}
.plan-body{margin:8px 6px 0;height:118px;background:var(--plan-grey);color:var(--white);font-size:11.5px;line-height:15px;text-align:center;padding:22px 26px;box-shadow:0 4px 6px rgba(0,0,0,.2)}
.plan.featured .plan-tab{background:linear-gradient(#ffe27a,var(--gold));color:#5a4300}
.plan.featured .plan-body{background:var(--blue)}

/* support */
.support{top:826px;left:138px;width:924px;height:360px}
.support-head{display:flex;align-items:center;gap:12px;font-size:26px;color:#8a8a8a;text-transform:uppercase}
.col-left{position:absolute;left:0;top:0;width:560px}
.col-right{position:absolute;left:617px;top:18px;width:307px}
.divider-v{position:absolute;left:587px;top:0;width:1px;height:350px;background:var(--line)}
.call-line{margin-top:32px;font-size:26px;font-weight:700;color:var(--ink)}
.call-line span,.ring-title span{color:var(--blue);font-weight:400}
.body-copy{font-size:12.5px;line-height:15.5px;color:#333;margin-top:8px}
.ticks li{display:flex;align-items:center;gap:14px;font-size:14px;font-weight:700;color:#333;height:29px}
.ticks svg{flex:none}
.ticks.first{margin-top:16px}
.right-title{font-size:19px;font-weight:700;color:var(--blue);line-height:27px;padding-bottom:12px;border-bottom:1px solid var(--line)}
.series li{display:flex;gap:14px;font-size:13px;font-weight:700;color:#333;line-height:17px;padding:14px 0 11px;border-bottom:1px solid var(--line)}
.series li svg{flex:none;margin-top:2px}
.right-note{font-size:12px;line-height:16px;color:#333;margin-top:16px}

/* ring */
.ring{top:1228px;left:138px;width:560px}
.ring-title{font-size:27px;font-weight:700;color:var(--ink);line-height:36px}
.ring .body-copy{margin-top:10px}
.ring .ticks{margin-top:10px}
.badge-247{top:1231px;left:755px;width:307px;height:151px;background:var(--blue);color:var(--white);text-align:center;font-family:"Roboto",Arial,sans-serif}
.badge-247 .big{font-size:52px;font-weight:500;line-height:62px;padding-top:8px}
.badge-247 .sub{font-size:31px;line-height:38px}
.chat-offer{top:1398px;left:761px;width:230px;font-size:19px;font-weight:700;color:var(--ink);line-height:27px}
.chat-btn{top:1459px;left:755px;width:257px;height:55px;background:var(--green);color:var(--white);font-family:"Roboto",Arial,sans-serif;font-size:36px;font-weight:500;line-height:55px;padding-left:18px}
.chat-agent{top:1422px;left:978px;width:84px;height:92px;border-radius:42px 42px 0 0;background:linear-gradient(#d8b79b,#3a3a3a)}
.soft-rule{top:1558px;left:138px;width:924px;height:8px;background:radial-gradient(ellipse at center top,rgba(0,0,0,.18),rgba(0,0,0,0) 70%)}

/* testimonials */
.testimonials{top:1613px;left:138px;width:924px;height:190px}
.quote-card{position:absolute;top:0;width:270px}
.avatar{width:80px;height:80px;border-radius:50%;border:3px solid #e3e3e3;background:linear-gradient(#f0e4da,#c99f84)}
.quote-name{position:absolute;left:101px;top:14px;font-size:22px;color:#555}
.quote-role{position:absolute;left:101px;top:48px;font-size:12px;color:var(--muted);padding-bottom:6px;border-bottom:1px solid var(--line);width:160px}
.quote-text{margin-top:26px;font-size:12px;line-height:18px;color:#444;padding-left:20px;position:relative}
.quote-text::before{content:"\201C";position:absolute;left:0;top:-6px;font-size:30px;color:#666}
.read-more{display:block;margin:20px 0 0 64px;width:138px;height:32px;background:var(--blue);color:var(--white);font-size:12px;font-weight:700;text-align:center;line-height:32px}

/* footers */
.footer-links{top:1838px;left:0;width:1200px;height:344px;background:var(--footer-dark);color:var(--white)}
.footer-links h2{position:absolute;left:138px;top:16px;font-size:21px;font-weight:700}
.link-col{position:absolute;top:64px;font-size:11px;line-height:22.7px}
.footer-info{top:2182px;left:0;width:1200px;height:210px;background:var(--footer-blue);color:var(--white)}
.info-col{position:absolute;top:20px}
.info-col h3{font-size:18px;font-weight:700;margin-bottom:12px;text-transform:uppercase}
.info-col li{font-size:11.5px;line-height:22px}
.contact li{display:flex;gap:12px;align-items:flex-start;margin-bottom:8px;line-height:16px}
.contact svg{flex:none}
.trust{position:absolute;left:860px;top:18px;width:202px}
.seal{background:#f2f2f2;border-radius:3px;margin:0 auto 8px}
.cards{display:flex;gap:4px;justify-content:center}
.cards span{width:38px;height:22px;border-radius:2px}
.copyright{top:2392px;left:0;width:1200px;height:36px;background:var(--footer-base);color:#ddd;font-size:11.5px;text-align:center;line-height:36px;letter-spacing:.5px}
</style>
</head>
<body>
<svg width="0" height="0" style="position:absolute">
  <defs>
    <symbol id="tick" viewBox="0 0 16 16">
      <rect x="1" y="1" width="14" height="14" fill="none" stroke="#2a86c4" stroke-width="1.6"/>
      <path d="M4 8.2l2.8 2.8L12.3 5" fill="none" stroke="#2a86c4" stroke-width="2"/>
    </symbol>
  </defs>
</svg>

<header class="site-header abs">
  <div class="brand abs"><span class="brand-mark"></span><span class="brand-name">eFixHaven</span></div>
  <div class="tollfree abs">
    <div class="tollfree-icon">
      <svg width="26" height="26" viewBox="0 0 24 24"><path d="M6.6 10.8a15.2 15.2 0 006.6 6.6l2.2-2.2c.3-.3.7-.4 1-.2 1.1.4 2.3.6 3.6.6.6 0 1 .4 1 1V20c0 .6-.4 1-1 1A17 17 0 013 4c0-.6.4-1 1-1h3.5c.6 0 1 .4 1 1 0 1.3.2 2.5.6 3.6.1.3 0 .7-.2 1z" fill="#fff"/></svg>
    </div>
    <div><div class="tollfree-label">CALL US TOLL FREE</div><div class="tollfree-number">1-800-555-0142</div></div>
  </div>
</header>

<section class="hero abs" role="img" aria-label="Customer service team wearing headsets, smiling agent in front">
  <p class="hero-caption abs">Lorem Ipsum is simply dummy sit dolor</p>
  <div class="hero-dots abs"><span></span><span></span><span class="on"></span><span></span></div>
</section>

<h2 class="section-title abs"><span>WHAT <em>WE OFFER</em></span></h2>

<div class="plans abs">
  <div class="plan"><div class="plan-tab">Silver Plan</div><p class="plan-body">Lorem Ipsum has been the industry's standard dummy text ever since the 1500s, when an unknown printer took a galley of type and scrambled it to make a type specimen book. It has survived not only five.</p></div>
  <div class="plan featured"><div class="plan-tab">Gold Plan</div><p class="plan-body">Lorem Ipsum has been the industry's standard dummy text ever since the 1500s, when an unknown printer took a galley of type and scrambled it to make a type specimen book. It has survived not only five.</p></div>
  <div class="plan"><div class="plan-tab">Platinum Plan</div><p class="plan-body">Lorem Ipsum has been the industry's standard dummy text ever since the 1500s, when an unknown printer took a galley of type and scrambled it to make a type specimen book. It has survived not only five.</p></div>
</div>

<section class="support abs">
  <div class="col-left">
    <h2 class="support-head">
      <svg width="26" height="34" viewBox="0 0 26 34"><circle cx="13" cy="9" r="8" fill="#9a9a9a"/><path d="M0 34c0-9 6-14 13-14s13 5 13 14z" fill="#9a9a9a"/></svg>
      Support for Varkeno Computer</h2>
    <p class="call-line">Call at <span>1-800-555-0142</span> for instant support.</p>
    <p class="body-copy">When you face a computer problem, identifying the problem and properly fixing it consumes precious time, labor, and resources. We are here to streamline the tech support process, offering high-quality, professional tech support for Varkeno computers. All of our technicians are fully certified and trained, with experience and expertise dealing specifically with Varkeno computers. Our technicians can efficiently deal with a range of problems and issues, including:</p>
    <ul class="ticks first">
      <li><svg width="16" height="16"><use href="#tick"/></svg>Diagnosis and repair of software issues</li>
      <li><svg width="16" height="16"><use href="#tick"/></svg>Troubleshooting software errors</li>
      <li><svg width="16" height="16"><use href="#tick"/></svg>Configuration services</li>
      <li><svg width="16" height="16"><use href="#tick"/></svg>Security program installation</li>
      <li><svg width="16" height="16"><use href="#tick"/></svg>Routine security maintenance</li>
    </ul>
  </div>
  <div class="divider-v"></div>
  <div class="col-right">
    <h3 class="right-title">We provide Varkeno support for a variety of Varkeno products, including:</h3>
    <ul class="series">
      <li><svg width="16" height="16"><use href="#tick"/></svg><span>Varkeno G Series, Varkeno 3000 V, Varkeno 3000 C, Varkeno 3000 N</span></li>
      <li><svg width="16" height="16"><use href="#tick"/></svg><span>Varkeno 3000 Y , Varkeno S Series, Varkeno SL Series, Varkeno R Series</span></li>
      <li><svg width="16" height="16"><use href="#tick"/></svg><span>Varkeno T Series, Varkeno X Series, Varkeno X Series Tablet, Varkeno W Series and more...</span></li>
    </ul>
    <p class="right-note">All service is done remotely in order to facilitate the fastest possible service and eliminate delays that cost your organization time and money. For fast and efficient Varkeno tech support, don't hesitate to contact us.</p>
  </div>
</section>

<section class="ring abs">
  <h2 class="ring-title">Just Give Us Ring At <span>1-800-555-0142</span> For Great Tech Support.</h2>
  <p class="body-copy">Platinum Plan - eFixHaven has "Platinum Plan" service for its honoured customers. Plan offers following features:</p>
  <ul class="ticks">
    <li><svg width="16" height="16"><use href="#tick"/></svg>We offer unlimited technical support</li>
    <li><svg width="16" height="16"><use href="#tick"/></svg>Support for antivirus, PC Clean-up and Optimization</li>
    <li><svg width="16" height="16"><use href="#tick"/></svg>We provide complete service for updating software and drivers</li>
    <li><svg width="16" height="16"><use href="#tick"/></svg>Support for CD/DVD burning, ZIP, Video players, Camera, MP3 players</li>
    <li><svg width="16" height="16"><use href="#tick"/></svg>Support for printers, scanners, WIFI and Networking setup</li>
    <li><svg width="16" height="16"><use href="#tick"/></svg>We ensure you that you will get fast resolutions</li>
  </ul>
</section>

<div class="badge-247 abs"><div class="big">24 x 7</div><div class="sub">Technical Support<br>for Varkeno Service</div></div>
<p class="chat-offer abs">FREE Issue Diagnosis by Expert Certified Techs</p>
<div class="chat-btn abs">LIVE CHAT</div>
<div class="chat-agent abs" role="img" aria-label="Support agent with headset"></div>
<div class="soft-rule abs"></div>

<section class="testimonials abs">
  <article class="quote-card" style="left:0">
    <div class="avatar" role="img" aria-label="Customer portrait"></div>
    <h4 class="quote-name">Perspiciatis</h4><p class="quote-role">Lorem Ipsum</p>
    <p class="quote-text">Lorem Ipsum is simply dummy text of the printing and typesetting industry.</p>
    <span class="read-more">READ MORE</span>
  </article>
  <article class="quote-card" style="left:313px">
    <div class="avatar" role="img" aria-label="Customer portrait"></div>
    <h4 class="quote-name">Voluptate</h4><p class="quote-role">Lorem Ipsum</p>
    <p class="quote-text">Lorem Ipsum is simply dummy text of the printing and typesetting industry.</p>
    <span class="read-more">READ MORE</span>
  </article>
  <article class="quote-card" style="left:657px">
    <div class="avatar" role="img" aria-label="Customer portrait"></div>
    <h4 class="quote-name">Architecto</h4><p class="quote-role">Lorem Ipsum</p>
    <p class="quote-text">Lorem Ipsum is simply dummy text of the printing and typesetting industry.</p>
    <span class="read-more">READ MORE</span>
  </article>
</section>

<footer class="footer-links abs">
  <h2>SUPPORT</h2>
  <ul class="link-col" style="left:138px">
    <li>&gt; Support for Slow PC</li><li>&gt; Support for Computer Issues</li><li>&gt; Support for PC Optimization</li><li>&gt; Support for PC Tuneup</li><li>&gt; Support for Macrel</li><li>&gt; Support for Adoro</li><li>&gt; Support for Flarex</li><li>&gt; Support for Registry</li><li>&gt; Support for Chromia</li><li>&gt; Support for Operix</li><li>&gt; Support for Safiro</li>
  </ul>
  <ul class="link-col" style="left:360px">
    <li>&gt; Support for Dorvane Computer</li><li>&gt; Support for Helpra Computer</li><li>&gt; Support Tosvik Computer</li><li>&gt; Support For Acryn Computer</li><li>&gt; Support For Varkeno Computer</li><li>&gt; Support for Solmi Computer</li><li>&gt; Support for Kompra Computer</li><li>&gt; Support for Linkora Router</li><li>&gt; Support for Belvor Router</li><li>&gt; Support for Ciskel Router</li><li>&gt; Support for Dalinq Router</li>
  </ul>
  <ul class="link-col" style="left:599px">
    <li>&gt; Support for Azuro Router</li><li>&gt; Support for Quorbel Antivirus</li><li>&gt; Support for Kasvel Antivirus</li><li>&gt; Support for Avrella Antivirus</li><li>&gt; Support for Avigo Antivirus</li><li>&gt; Support for Avestra Antivirus</li><li>&gt; Support for Nortavi AntiVirus</li><li>&gt; Support for ByteWarden Antivirus</li><li>&gt; Support for Dorvane Printer</li><li>&gt; Support for Helpra Printer</li><li>&gt; Support for Brothwell Printer</li>
  </ul>
  <ul class="link-col" style="left:850px">
    <li>&gt; Support for Panorix Printer</li><li>&gt; Support for Epsura Printer</li><li>&gt; Support for Canvo Printer</li><li>&gt; Support for Samvira Printer</li><li>&gt; Support for Netgrove Router</li><li>&gt; Support for Pogli Games</li><li>&gt; Support for Webrill Antivirus</li><li>&gt; Support for Vipora Antivirus</li><li>&gt; Support for Trenmik Antivirus</li><li>&gt; Support for Totalguard Antivirus</li><li>&gt; Support for Pandrel Antivirus</li><li>&gt; Support for Printers</li>
  </ul>
</footer>

<footer class="footer-info abs">
  <div class="info-col" style="left:138px">
    <h3>Quick Links</h3>
    <ul><li>&gt; About Us</li><li>&gt; Contact Us</li><li>&gt; Terms &amp; Conditions</li><li>&gt; Privacy Policy</li><li>&gt; Refund Policy</li><li>&gt; Disclaimer</li></ul>
  </div>
  <div class="info-col contact" style="left:372px">
    <h3>Contact Info</h3>
    <ul>
      <li><svg width="14" height="18" viewBox="0 0 14 18"><path d="M7 0a7 7 0 00-7 7c0 5 7 11 7 11s7-6 7-11a7 7 0 00-7-7zm0 9.5A2.5 2.5 0 117 4.5a2.5 2.5 0 010 5z" fill="#fff"/></svg><span>18 Birch Lane, Millbrook, NY<br>10000, USA.</span></li>
      <li><svg width="16" height="16" viewBox="0 0 16 16"><circle cx="8" cy="8" r="7" fill="none" stroke="#fff" stroke-width="1.5"/><path d="M5 4.5l1.5 2-1 1a6 6 0 003 3l1-1 2 1.5-1 1.5c-3 0-6.5-3.5-6.5-6.5z" fill="#fff"/></svg><span>1-800-555-0142</span></li>
      <li><svg width="16" height="16" viewBox="0 0 16 16"><rect x="2" y="5" width="12" height="9" fill="none" stroke="#fff" stroke-width="1.5"/><path d="M4 5V2h8v3" fill="none" stroke="#fff" stroke-width="1.5"/></svg><span>212-555-0187</span></li>
      <li><svg width="16" height="14" viewBox="0 0 16 14"><rect x="1" y="2" width="14" height="10" fill="none" stroke="#fff" stroke-width="1.5"/><path d="M1 2l7 6 7-6" fill="none" stroke="#fff" stroke-width="1.5"/></svg><span>support@efixhaven.example</span></li>
    </ul>
  </div>
  <div class="info-col" style="left:670px">
    <h3>Plans</h3>
    <ul><li>&gt; Silver Plan</li><li>&gt; Gold Plan</li><li>&gt; Platinum Plan</li></ul>
  </div>
  <div class="trust" role="img" aria-label="Safenook trust seal, payment seal, verified and secured seal, accepted payment cards">
    <div class="seal" style="width:90px;height:44px"></div>
    <div class="seal" style="width:62px;height:30px"></div>
    <div class="seal" style="width:96px;height:32px"></div>
    <div class="cards"><span style="background:#e8e8e8"></span><span style="background:#f0c23a"></span><span style="background:#e9eef7"></span><span style="background:#f3f3f3"></span><span style="background:#cfe0f2"></span></div>
  </div>
</footer>

<div class="copyright abs">© 2014 EFIXHAVEN &nbsp; | &nbsp; All Rights Reserved</div>
</body>
</html>
```